Food Package Design (Soybean Rice Nuggets)

We Need package design for our new item. Here's detail:

BAG DIMENSION:
62/4 X 10 1/2 X 3 1/2 INCH
STAND UP BAG (ATTACHED PIC)
ARTWORK TEMPLATE ATTACHED (Please erase the contents in the attached template. Use the teamplte only).
At the end of the project, I will need printable, editable file with print die line

<Front side package>
The Crispy Crunchy Soybean Rice Nuggets
Belvri TM logo on top (*FILE UPLOADED)

Gluten Free
No Trans Fat
No Cholesterol
Net Weight 5 oz (142g)

<Back Side>
Soft and chewy rice puffs covered with roasted soybean powders. Belvri’s Soybean Rice Nuggets hit the other end of the spectrum. These are light, crunchy, crispy and savory and make a delicious that you might not be able to stop eating.

Ingredients: rice powder, palm oil, soybean powder, salt, sugar, corn grits

Contains soybean

Manufactured exclusively for Belvri (logo)
Tarrowfield, CA 90000
Made in Korea

www.belvrisnacks.example

Nutrition Facts (*File uploaded)
Serving Size 30g
Seriving Per Container About 5
Calories 140
Calories from Fat 45
Total Fat 5g 8%
Saturated Fat 2.5g 13%
Trans Fat 0g
Cholesterol 0mg 0%
Sodium 30mg 1%
Total Carbohydrate 22g 7%
Dietary Fiber 0g 0%
Sugars 4g
Protein 2g

Vitamin A 0%
Vitamin C 0%
Calcium 0%
Iron 0%

Barcode (*FILE UPLOADED)

* If I find a design I like, I could end my project earlier than deadline. I prefer to end the project sooner than deadline!
*If you need any images to purchase, please let me know.
Thank you for your participation and interest in our project!

Target Market(s)

HEALTH CONSCIOUS CONSUMERS, CONSUMER WHO LOVE SNACKING AND ALWAYS LOOKING FOR INNOVATIVE, UNIQUE, HEALTHY SNACKS.

Requirements
Must have
• FUN, BOLDNESS, MODERN, PLAYFUL, EYE CATCHING DESIGN

```html
<!DOCTYPE html>
<html lang="en">
<head>
<meta charset="utf-8">
<title>Belvri Soybean Rice Nuggets – Front Panel</title>
<link rel="stylesheet" href="https://fonts.googleapis.com/css2?family=Grandstander:wght@700;800&family=Lora:ital@1&display=swap">
<style>
  :root {
    --stage: #ececec;
    --amber-deep: #f2a414;
    --amber-mid: #f8bb22;
    --amber-light: #fcd73f;
    --ink: #262626;
    --ink-soft: #3a3a3a;
    --plate-light: #f4f4f2;
    --plate-shade: #c9c3b8;
    --badge-gold: #e8a63a;
    --badge-red: #d8463b;
    --badge-green: #6faa4a;
    --badge-text: #ffffff;
  }
  html, body {
    margin: 0;
    padding: 0;
    width: 1200px;
    height: 1182px;
    overflow: hidden;
    background: var(--stage);
  }
  .canvas {
    display: block;
    width: 1200px;
    height: 1182px;
  }
  .brand-name {
    font-family: "Grandstander", "Comic Sans MS", cursive;
    font-weight: 800;
    font-size: 66px;
    fill: var(--ink);
  }
  .product-title {
    font-family: "Grandstander", "Comic Sans MS", cursive;
    font-weight: 700;
    font-size: 44px;
    fill: var(--ink-soft);
  }
  .claim-text {
    font-family: "Grandstander", "Comic Sans MS", cursive;
    font-weight: 800;
    font-size: 10px;
    fill: var(--badge-text);
    text-anchor: middle;
  }
  .net-weight {
    font-family: "Lora", Georgia, serif;
    font-style: italic;
    font-size: 10px;
    fill: var(--ink);
    text-anchor: middle;
  }
</style>
</head>
<body>
<svg class="canvas" viewBox="0 0 1200 1182" xmlns="http://www.w3.org/2000/svg">
  <defs>
    <linearGradient id="pouch-fill" x1="0" y1="0" x2="1" y2="0.3">
      <stop offset="0" stop-color="var(--amber-deep)"/>
      <stop offset="0.55" stop-color="var(--amber-mid)"/>
      <stop offset="1" stop-color="var(--amber-light)"/>
    </linearGradient>
    <radialGradient id="snack-photo-tone" cx="0.5" cy="0.5" r="0.6">
      <stop offset="0" stop-color="#d98a3a"/>
      <stop offset="0.45" stop-color="#8a7560"/>
      <stop offset="0.75" stop-color="var(--plate-shade)"/>
      <stop offset="1" stop-color="var(--plate-light)"/>
    </radialGradient>
    <clipPath id="pouch-shape">
      <rect x="280" y="40" width="640" height="1105" rx="14"/>
    </clipPath>
    <path id="title-arc" d="M 318 463 A 285 360 0 1 1 450 1095"/>
  </defs>

  <g class="pouch-front" clip-path="url(#pouch-shape)">
    <rect class="pouch-base" x="280" y="40" width="640" height="1105" fill="url(#pouch-fill)"/>

    <path class="corner-band corner-band--top" d="M 280 40 L 575 40 Q 380 110 280 262 Z" fill="var(--ink)"/>
    <path class="corner-band corner-band--bottom" d="M 920 908 L 920 1145 L 668 1145 Q 840 1060 920 908 Z" fill="var(--ink)"/>

    <line x1="280" y1="96" x2="920" y2="96" stroke="#000" stroke-opacity="0.08" stroke-width="2"/>
    <line x1="280" y1="168" x2="920" y2="168" stroke="#000" stroke-opacity="0.1" stroke-width="3"/>
    <line x1="280" y1="176" x2="920" y2="176" stroke="#fff" stroke-opacity="0.18" stroke-width="2"/>

    <ellipse class="window-ring" cx="480" cy="790" rx="200" ry="290" fill="none" stroke="var(--ink)" stroke-width="1.4"/>
    <ellipse class="window-ring" cx="480" cy="790" rx="222" ry="308" fill="none" stroke="var(--ink)" stroke-width="1.2"/>

    <ellipse class="product-window" cx="480" cy="790" rx="180" ry="268" fill="url(#snack-photo-tone)"
             role="img" aria-label="Photo of golden soybean rice nuggets piled in a dark square stoneware dish on a white surface"/>

    <text class="brand-name" x="600" y="292" text-anchor="middle">Belvri</text>

    <text class="product-title">
      <textPath href="#title-arc" textLength="1150" lengthAdjust="spacing">The Crispy Crunchy Soybean Rice Nuggets</textPath>
    </text>

    <g class="claim-badge">
      <circle cx="850" cy="770" r="28" fill="var(--badge-gold)"/>
      <text class="claim-text" x="850" y="767">GLUTEN</text>
      <text class="claim-text" x="850" y="779">FREE</text>
    </g>
    <g class="claim-badge">
      <circle cx="850" cy="836" r="28" fill="var(--badge-red)"/>
      <text class="claim-text" x="850" y="833">NO TRANS</text>
      <text class="claim-text" x="850" y="845">FAT</text>
    </g>
    <g class="claim-badge">
      <circle cx="850" cy="902" r="28" fill="var(--badge-green)"/>
      <text class="claim-text" x="850" y="899">NO</text>
      <text class="claim-text" x="850" y="911" style="font-size:8.5px">CHOLESTEROL</text>
    </g>

    <text class="net-weight" x="850" y="948">Net Weight 5 Oz</text>
    <text class="net-weight" x="850" y="961">(142g)</text>
  </g>
</svg>
</body>
</html>
```